Health care startup that needs to WOW bone marrow doctors with presentation brochure

We need a brochure to compliment our in person presentation to Transplant Hospital Directors. The design needs to feel contemporary and clean. We need to convey a very professional operation that embraces technology. We want to break in as a modern company in an industry that has historically been non-profit and a little dull.

Our website is corvantix.com

I've included an early brochure we had from our site. We like our logo. The "Corvantix blue" in the logo is #7CD9DA in Microsoft Office products

I envision the brochure having two folds to reveal three pages. Ive added some of the text and images we will use.

The charts and graphs included in the attached ppt. can be modified by the designer but we want to capture the information in the final design.

Target Market(s)

Transplant Center Physicians

Industry/Entity Type

Healthcare

Colors
85cae6

Requirements
Must have
• a foldout brochure with at least three pages.
• Emphasis on our key competitive advantages, minority donors (80%), predominantly male (70%) and average age 21. This needs to be emphasized.
• I want to show that we will be a cost leader in the industry as well.
Nice to have
• I like the idea of a pocket or some means to attach a personal letter to clients on the inside. Not sure if that would work with the flow of the document.
• Websites whose design we LOVE:
• http://www.drelvonsuite.com/solutions/overview/
• http://quorelbay.com/
Should not have
• I dont want plain stock photos of people looking straight at a camera smiling. This feels like a non-profit trying to elict sympathy. Compassion for patients in a core value of the company, but it should still feel like something that is modern and new and a change to the current industry

```html
<!DOCTYPE html>
<html lang="en">
<head>
<meta charset="utf-8">
<title>Corvantix Brochure Spread</title>
<link href="https://fonts.googleapis.com/css2?family=Didact+Gothic&family=Mulish:wght@600;800&display=swap" rel="stylesheet">
<style>
  :root{
    --teal:#5fd0d4;
    --teal-light:#8fe0e2;
    --teal-deep:#3cb7bd;
    --panel:rgba(40,150,160,.35);
    --ink:#173a40;
    --ink-soft:#244a50;
    --band:#585858;
    --white:#ffffff;
    --chart-bg:#e7e8e9;
    --badge-red:#d9413c;
  }
  *{box-sizing:border-box;margin:0;padding:0}
  html,body{width:1200px;height:978px;overflow:hidden;background:#d2d2d2}
  body{font-family:"Didact Gothic",sans-serif;color:var(--ink)}
  .spread{position:relative;width:1200px;height:978px;display:flex}
  .page{position:relative;width:600px;height:978px;overflow:hidden;
    background:radial-gradient(circle at 30% 40%,var(--teal-light),var(--teal) 55%,var(--teal-deep))}
  .page--right{background:radial-gradient(circle at 70% 55%,var(--teal-light),var(--teal) 60%,var(--teal-deep))}
  .abs{position:absolute}
  h2{font-family:"Didact Gothic",sans-serif;font-weight:400;color:var(--ink)}
  .rule{border-bottom:1.5px solid var(--ink);padding-bottom:3px}

  /* left page */
  .about{left:18px;top:24px;width:130px}
  .about h2{font-size:23px}
  .about p{font-size:12.5px;line-height:1.35;margin-top:10px}
  .divider{left:164px;top:22px;width:1.5px;height:200px;background:var(--ink)}
  .what{left:180px;top:22px;width:404px}
  .what h2{font-size:23px;width:190px}
  .what p{font-size:12px;line-height:1.42;text-align:justify;margin-top:8px}
  .product{left:18px;top:268px;width:290px}
  .product h2{font-size:23px;width:170px}
  .product p{font-size:13px;line-height:1.4;margin-top:12px;text-align:justify}
  .product ul{list-style:none;margin-top:12px;font-size:10px;line-height:1.45}
  .product li::before{content:"• "}
  .product li.sub{padding-left:18px}
  .product li.sub::before{content:"✓ "}
  .badges{display:flex;gap:6px;margin:10px 0 0 95px}
  .badge{width:38px;height:36px;background:var(--white);border:3px solid var(--badge-red);border-radius:4px}
  .badge--round{border-radius:50%}
  .badge--wide{width:56px;height:26px;margin-top:6px;border-radius:3px}
  .left-art{left:0;top:590px;width:600px;height:388px;z-index:1}
  .why{left:316px;top:252px;width:284px;height:430px;background:var(--panel);padding:14px 12px 0 4px;z-index:2}
  .why h2{font-size:21px;text-align:center;border-bottom:1.5px solid var(--ink);padding-bottom:4px;margin-left:10px}
  .why dl{margin-top:6px}
  .why dt{font-size:16px;margin-top:9px;display:flex;align-items:center;gap:6px}
  .why dt svg{flex:none}
  .why dd{font-size:11.5px;line-height:1.4;margin-left:25px;margin-top:3px}

  /* right page */
  .right-art{left:0;top:0;width:600px;height:340px}
  .registries{left:18px;top:18px;width:300px;z-index:2}
  .registries h2{font-size:21px;line-height:1.3}
  .registries ul{list-style:none;font-size:13.5px;line-height:1.33;margin-top:12px}
  .registries li.cont{padding-left:46px}
  .strip{left:0;top:334px;width:600px;height:112px;background:var(--white);padding:10px 30px;
    display:grid;grid-template-columns:repeat(8,1fr);gap:8px 10px;align-items:center}
  .mark{font-size:10px;color:var(--ink-soft);display:flex;align-items:center;gap:4px;line-height:1.1}
  .mark i{width:12px;height:12px;background:var(--teal-deep);flex:none}
  .mark--wide{grid-column:span 2}
  .dot{width:30px;height:30px;border-radius:50%;border:2px solid var(--teal-deep);justify-self:center}
  .results-title{left:0;top:458px;width:600px;text-align:center;font-family:"Mulish",sans-serif;font-weight:800;font-size:24px;color:var(--ink)}
  .results{left:41px;top:494px;width:516px;height:292px;background:var(--chart-bg)}
  .chart-head{position:absolute;top:18px;font-family:Georgia,serif;font-size:11.5px;text-decoration:underline;font-weight:700}
  .chart-split{position:absolute;left:262px;top:22px;width:1px;height:200px;background:#333}
  .tagline{position:absolute;left:0;bottom:0;width:100%;height:34px;background:var(--white);
    text-align:center;font-size:17px;line-height:34px;color:var(--ink)}
  .partners-title{left:0;top:800px;width:600px;text-align:center;font-family:"Mulish",sans-serif;font-weight:800;font-size:24px;color:#1d3b3d}
  .partners{left:37px;top:836px;width:521px;height:128px;background:var(--white);padding:10px 14px;
    display:grid;grid-template-columns:1fr 1fr 1fr;grid-template-rows:62px 50px;gap:0 14px;align-items:center}
  .partner{font-family:"Mulish",sans-serif;font-weight:800;font-size:16px;color:#1e6f95;display:flex;align-items:center;gap:6px}
  .partner i{width:14px;height:14px;background:#1e6f95;flex:none}
  .partner--box{background:#2a88c4;color:var(--white);height:56px;padding:0 10px;font-size:14px}
  .partner--small{font-size:12px;font-weight:600}
  .partners p{grid-column:2 / span 2;font-size:11.5px;line-height:1.35;color:var(--ink)}
</style>
</head>
<body>
<main class="spread">

  <section class="page page--left">
    <div class="abs about">
      <h2 class="rule">About Us:</h2>
      <p>Corvantix is an independent bone marrow registry focused on finding donors for African American, Asian, and Hispanic patients. We are currently based out of Washington DC.</p>
    </div>
    <div class="abs divider"></div>
    <div class="abs what">
      <h2 class="rule">What we Do</h2>
      <p>As a total transplant procurement solution, Corvantix vertically integrates as a registry and donation center to maximize efficiency and provide operational excellence to deliver marrow/PBSCs on time - at industry leading prices. Corvantix harnesses industry leading best practices to target, recruit, and maintain active donors with unprecedented donor follow through rates. Transplant Center clients access these donors through our web based software, Stratalink. Once identified as a potential match, Corvantix guides donors through CT, workup, and collection. We then personally deliver the product to our transplant center clients.</p>
    </div>

    <div class="abs product">
      <h2 class="rule">Stratalink</h2>
      <p>Transplant Centers match their patients to Corvantix donors on Stratalink, developed by Kelmark, an Industry leader used in numerous international registries</p>
      <ul>
        <li>Integration with Global Marrow Donor Index and</li>
        <li>Continental Marrow Donor Exchange (CMDEX).</li>
        <li>Complies with International Marrow Donor Council</li>
        <li>Verified FDA compliant by independent consulting audit</li>
        <li>ISO accreditation requested by AMR</li>
        <li class="sub">9001 (Quality Management System)</li>
        <li class="sub">27001 (Information Security Management System)</li>
        <li class="sub">SOPs, project plans</li>
        <li>Guarantees for testing, validation, security, etc.</li>
      </ul>
      <div class="badges">
        <span class="badge"></span>
        <span class="badge"></span>
        <span class="badge badge--round"></span>
        <span class="badge badge--wide"></span>
      </div>
    </div>

    <aside class="abs why">
      <h2>Why Choose Corvantix</h2>
      <dl>
        <dt><svg width="14" height="14" viewBox="0 0 14 14"><rect x="1" y="1" width="12" height="12" fill="none" stroke="#173a40" stroke-width="1.4"/><path d="M3.5 7l2.5 2.5 5-6" fill="none" stroke="#173a40" stroke-width="1.6"/></svg>Efficient</dt>
        <dd>Increase donor availability from our domestically sourced registry; Reducing cycle time from donor contact to HCT/P delivery.</dd>
        <dt><svg width="14" height="14" viewBox="0 0 14 14"><rect x="1" y="1" width="12" height="12" fill="none" stroke="#173a40" stroke-width="1.4"/><path d="M3.5 7l2.5 2.5 5-6" fill="none" stroke="#173a40" stroke-width="1.6"/></svg>Targeted</dt>
        <dd>Donor base recruitment focusing on minority males (18-25 year old).</dd>
        <dt><svg width="14" height="14" viewBox="0 0 14 14"><rect x="1" y="1" width="12" height="12" fill="none" stroke="#173a40" stroke-width="1.4"/><path d="M3.5 7l2.5 2.5 5-6" fill="none" stroke="#173a40" stroke-width="1.6"/></svg>Responsive</dt>
        <dd>24/7 access to a personal Corvantix donation coordinator: from initial match to HCT/P delivery.</dd>
        <dt><svg width="14" height="14" viewBox="0 0 14 14"><rect x="1" y="1" width="12" height="12" fill="none" stroke="#173a40" stroke-width="1.4"/><path d="M3.5 7l2.5 2.5 5-6" fill="none" stroke="#173a40" stroke-width="1.6"/></svg>Intelligent</dt>
        <dd>Secure, intuitive website to easily search the Corvantix database and monitor donations in progress.</dd>
        <dt><svg width="14" height="14" viewBox="0 0 14 14"><rect x="1" y="1" width="12" height="12" fill="none" stroke="#173a40" stroke-width="1.4"/><path d="M3.5 7l2.5 2.5 5-6" fill="none" stroke="#173a40" stroke-width="1.6"/></svg>Professional</dt>
        <dd>HCT/P transport provided by a dedicated Corvantix team member.</dd>
      </dl>
    </aside>

    <svg class="abs left-art" viewBox="0 0 600 388" preserveAspectRatio="none">
      <defs>
        <linearGradient id="leftPhoto" x1="0" y1="0" x2="1" y2="1">
          <stop offset="0" stop-color="#f3f5f6"/>
          <stop offset=".6" stop-color="#c9d4d8"/>
          <stop offset="1" stop-color="#7f98a3"/>
        </linearGradient>
      </defs>
      <path d="M0 0 C150 10 380 40 600 108 L600 128 C380 64 160 36 0 30 Z" fill="var(--band)"/>
      <path d="M0 34 C140 40 330 60 600 130 L600 150 C330 84 140 60 0 56 Z" fill="var(--teal-deep)"/>
      <g role="img" aria-label="Photo of a clinician taking an older patient's blood pressure">
        <path d="M0 60 C130 64 290 84 420 118 L420 388 L0 388 Z" fill="url(#leftPhoto)"/>
      </g>
    </svg>
  </section>

  <section class="page page--right">
    <svg class="abs right-art" viewBox="0 0 600 340" preserveAspectRatio="none">
      <defs>
        <linearGradient id="rightPhoto" x1="0" y1="0" x2="1" y2="1">
          <stop offset="0" stop-color="#e6eef2"/>
          <stop offset=".55" stop-color="#cdd9df"/>
          <stop offset="1" stop-color="#8fa8b4"/>
        </linearGradient>
      </defs>
      <path d="M220 0 L600 0 L600 318 C470 312 360 268 310 195 C275 140 240 75 220 0 Z" fill="var(--band)"/>
      <g role="img" aria-label="Photo of a lab technician in gloves holding a blood sample tube">
        <path d="M238 0 L600 0 L600 298 C480 292 375 250 328 182 C295 132 258 70 238 0 Z" fill="url(#rightPhoto)"/>
      </g>
    </svg>

    <div class="abs registries">
      <h2>International<br>Registries<br>Utilizing<br>Stratalink</h2>
      <ul>
        <li>2007: Czech Republic, Slovakia</li>
        <li>2008: Cyprus, Bulgaria, Vistula Poland</li>
        <li>2009: South Africa, Finland</li>
        <li>2010: Sweden, Denmark, Slovenia, Israel</li>
        <li>2011: Hungary, Argentina, Great Britain (AMR),</li>
        <li class="cont">Belgium, Ireland, Saudi Arabia</li>
        <li>2012: Nigeria, Cordlink, …</li>
      </ul>
    </div>

    <div class="abs strip">
      <span class="mark mark--wide"><i></i>Albion Blood Service</span>
      <span class="mark mark--wide"><i></i>Nordvik University Hospital</span>
      <span class="dot"></span>
      <span class="dot"></span>
      <span class="mark"><i></i>Kaleva Blood Service</span>
      <span class="mark"><i></i>Eskil Registret</span>
      <span class="dot"></span>
      <span class="dot"></span>
      <span class="mark"><i></i>Solvai</span>
      <span class="dot"></span>
      <span class="dot"></span>
      <span class="dot"></span>
      <span class="dot"></span>
      <span class="dot"></span>
    </div>

    <h2 class="abs results-title">Donor Recruitment Results</h2>
    <div class="abs results">
      <span class="chart-head" style="left:48px">Number of Recruited Donors</span>
      <span class="chart-head" style="left:292px">Donor Ethnicity Composition</span>
      <div class="chart-split"></div>
      <svg class="abs" style="left:28px;top:44px" width="220" height="190" viewBox="0 0 220 190">
        <g font-family="Didact Gothic, sans-serif" font-size="10" fill="#222">
          <text transform="translate(12 20) rotate(90)">2000</text>
          <text transform="translate(12 52) rotate(90)">1500</text>
          <text transform="translate(12 84) rotate(90)">1000</text>
          <text transform="translate(12 122) rotate(90)">500</text>
          <text transform="translate(12 162) rotate(90)">0</text>
        </g>
        <g stroke="#333" stroke-width="1">
          <line x1="22" y1="24" x2="172" y2="24"/>
          <line x1="22" y1="56" x2="172" y2="56"/>
          <line x1="22" y1="88" x2="172" y2="88"/>
          <line x1="22" y1="126" x2="172" y2="126"/>
          <line x1="22" y1="166" x2="172" y2="166"/>
        </g>
      </svg>
      <div class="tagline">Corvantix is on track to register 10,000 donors in 2016</div>
    </div>

    <h2 class="abs partners-title">Our Partners</h2>
    <div class="abs partners">
      <span class="partner partner--box">Tessora Labs</span>
      <span class="partner"><i></i>KELMARK</span>
      <span class="partner partner--small"><i></i>Halden Apheresis Associates</span>
      <span class="partner partner--small"><i></i>Brightwell Donor Fund</span>
      <p>(Corvantix has partnered with industry leaders for efficient donor CT, workup, and collection of PBSC and marrow.)</p>
    </div>
  </section>

</main>
</body>
</html>
```